Website design needed for gift based dropship website

I am building a dropshipping website that will create gift based merchandise and send it out to our clients customers for them. Our clients will sell products and when a customer buys from them, we create the item and send it out to the customer.

I am looking for a very similar website to brindlow.com - that website is doing a very similar thing to what i am doing but where the brindlow website is based around clothing, my website will be based around gifts. Another website that i like that is doing a similar thing to what i will do is vemtar.com

I require 2 pages to be made:
1) The home page
2) A landing page for a free product giveaway offer

1) THE HOME PAGE
The home page should be a merger of the two previously stated websites (www.vemtar.com and www.brindlow.com). The style fo the homepage should be based on the logo that is attached and the colour scheme should be similar but basic.

2) THE LANDING PAGE
The landing page will be giving away a free mobile phone cover. The page needs to have some mobile phone covers for different phones all with random designs on. The page should state that they can have any design that they want and they do not pay for the phone (they only pay for shipping).

Menu pages and text should be taken from the brindlow.com website.

18 - 40 year old males. People who like the idea of earning extra money in their spare time but aren't too sure how to do it. Semi-professional jobs.

2 page

• A "how it works" image where the dropshipping process is explained to a visitor to the website (similar to the one on the brindlow "how it works page")
• Testimonial area on homepage
• Homepage should not have:
• - "latest orders from" area
• - Video
• - Warehousing/fulfilment area
• - Integration area
• -

```html
<!DOCTYPE html>
<html lang="en">
<head>
<meta charset="utf-8">
<title>Merrow Prints – On-demand gift printing</title>
<link rel="stylesheet" href="https://fonts.googleapis.com/css2?family=Oswald:wght@400;500;600&family=Source+Sans+Pro:wght@400;600&display=swap">
<style>
:root{
  --red:#e2342b;
  --red-dark:#a51c1c;
  --maroon:#3b1516;
  --ink:#333;
  --muted:#6f6f6f;
  --line:#e4e4e4;
  --soft:#f4f4f4;
  --white:#fff;
}
*{box-sizing:border-box;margin:0;padding:0}
html,body{width:1200px;height:3651px;overflow:hidden}
body{font-family:"Source Sans Pro",Arial,sans-serif;color:var(--ink);background:var(--white);position:relative;font-size:13px}
.abs{position:absolute}
.head{font-family:"Oswald",Arial,sans-serif;text-transform:uppercase;color:var(--maroon);font-weight:500}
.center{text-align:center}
.section-title{position:absolute;left:0;width:1200px;text-align:center;font-size:22px;line-height:28px}
.section-sub{position:absolute;left:0;width:1200px;text-align:center;color:var(--muted);font-size:14px;line-height:18px}
.btn{position:absolute;font-family:"Oswald",Arial,sans-serif;text-transform:uppercase;font-size:13px;display:flex;align-items:center;justify-content:center;letter-spacing:.3px}
.btn-red{background:var(--red);color:var(--white)}
.btn-line{border:2px solid #bdbdbd;color:#777;background:var(--white)}
.brand{font-family:"Oswald",Arial,sans-serif;font-weight:600;color:var(--red);text-transform:uppercase;display:flex;align-items:center;gap:8px}
.brand-dot{width:22px;height:22px;border-radius:50%;background:var(--red)}

/* header */
.site-header{position:absolute;top:0;left:0;width:1200px;height:68px;border-bottom:1px solid var(--line);background:var(--white)}
.site-header .brand{left:234px;top:14px;font-size:21px;line-height:1}
.topbar{left:686px;top:6px;font-size:10px;color:var(--muted);display:flex;gap:22px;text-transform:uppercase}
.topbar b{color:var(--red)}
.main-nav{left:560px;top:38px;display:flex;gap:20px;font-family:"Oswald",Arial,sans-serif;font-size:13px;text-transform:uppercase;color:var(--ink)}
.main-nav .active{color:var(--red);border-bottom:2px solid var(--red);padding-bottom:6px;padding-right:4px}

/* hero */
.hero{position:absolute;top:68px;left:0;width:1200px;height:322px;background:#f7f7f7}
.ribbon{left:510px;top:34px;width:180px;height:24px;background:var(--red);color:var(--white);font-family:"Oswald",Arial,sans-serif;font-size:14px;display:flex;align-items:center;justify-content:center;clip-path:polygon(0 0,100% 0,94% 50%,100% 100%,0 100%,6% 50%)}
.hero-title{top:66px;left:0;width:1200px;font-size:32px;line-height:38px;font-weight:600}
.hero-sub{top:108px;left:0;width:1200px;font-size:15px;line-height:18px;color:var(--muted)}
.hero-gifts{left:419px;top:219px;width:365px;height:103px;background:linear-gradient(90deg,#f2c9c3,#e8e8e8 45%,#f2c9c3);border-radius:3px 3px 0 0}

/* split */
.split{position:absolute;top:390px;left:0;width:1200px;height:189px}
.split-half{position:absolute;top:0;width:600px;height:189px}
.split-half h3{position:absolute;top:30px;width:100%;text-align:center;font-size:16px;line-height:22px}
.split-half p{position:absolute;top:62px;left:190px;width:220px;text-align:center;color:var(--muted);font-size:13px;line-height:1.45}
.split-or{left:586px;top:76px;width:28px;height:28px;border-radius:50%;background:var(--white);font-family:"Oswald",Arial,sans-serif;font-size:11px;display:flex;align-items:center;justify-content:center;color:var(--maroon)}

/* products */
.products{position:absolute;top:579px;left:0;width:1200px;height:747px}
.product-card{position:absolute;width:176px;height:248px;border:1px solid var(--line);background:var(--white)}
.product-art{position:absolute;left:30px;top:18px;width:114px;height:150px;border-radius:4px}
.product-label{position:absolute;left:0;bottom:0;width:100%;height:60px;background:#f1f1f1;text-align:center;padding-top:14px}
.product-label h4{font-size:13px;line-height:17px;font-weight:500}
.product-label span{font-size:11px;color:var(--muted)}
.product-label span b{color:var(--red);font-weight:400}
.product-card.is-featured .product-label{background:var(--red);text-align:left;padding-left:12px}
.product-card.is-featured h4,.product-card.is-featured span,.product-card.is-featured span b{color:var(--white)}
.go{right:12px;top:17px;width:26px;height:26px;border:2px solid var(--white);border-radius:50%}

/* how it works */
.how{position:absolute;top:1326px;left:0;width:1200px;height:390px;background:#f6f6f6;overflow:hidden}
.how-wedge{left:0;top:0;width:1200px;height:390px;background:#fbfbfb;clip-path:polygon(0 0,100% 0,100% 58%,50% 100%,0 58%)}
.step{position:absolute;top:190px;width:240px;text-align:center}
.step-ring{position:absolute;width:120px;height:120px;border:2px solid var(--red);border-radius:50%;top:-76px;background:var(--white)}
.step-art{position:absolute;left:28px;top:28px;width:60px;height:60px;border-radius:50%;background:#f6d6d3}
.step h4{color:var(--red);font-size:15px;line-height:20px;font-weight:400;margin-top:62px}
.step p{font-size:12.5px;line-height:1.5;color:var(--muted);margin-top:6px}
.step-arrow{top:169px;width:84px;height:10px}

/* testimonials */
.testimonials{position:absolute;top:1716px;left:0;width:1200px;height:504px}
.quote-mark{left:573px;top:100px;width:54px;height:54px;border:2px solid var(--red);border-radius:50%;color:var(--red);font-family:"Oswald",Arial,sans-serif;font-size:40px;display:flex;align-items:center;justify-content:center;line-height:1;padding-top:14px}
.review{position:absolute;top:180px;width:229px;height:180px;background:var(--white);box-shadow:0 1px 6px rgba(0,0,0,.12);text-align:center;padding:22px 18px 0}
.stars{color:var(--red);font-size:13px;letter-spacing:2px}
.review p{margin-top:12px;font-size:12px;line-height:1.55;color:var(--muted)}
.reviewer{position:absolute;top:370px;width:229px;text-align:center;color:var(--red);font-family:"Oswald",Arial,sans-serif;font-size:11px;text-transform:uppercase}

/* different */
.different{position:absolute;top:2220px;left:0;width:1200px;height:392px;background:linear-gradient(90deg,#7e1414 0%,#b3201d 45%,#e2342b 100%)}
.different .section-title,.different .section-sub{color:var(--white)}
.different .section-title{left:240px;width:900px}
.different .section-sub{left:240px;width:900px}
.person-photo{left:182px;top:20px;width:293px;height:372px;background:linear-gradient(180deg,#c9a08a 0%,#8f6a58 40%,#c9a27a 70%,#b58a63 100%);border-radius:140px 140px 0 0;opacity:.85}
.feature{position:absolute;width:230px;color:var(--white)}
.feature .num{position:absolute;left:0;top:-6px;font-family:"Oswald",Arial,sans-serif;font-size:26px;line-height:34px}
.feature h4{margin-left:36px;font-family:"Oswald",Arial,sans-serif;font-size:12.5px;line-height:17px;font-weight:500;text-transform:uppercase}
.feature p{margin-left:36px;margin-top:6px;font-size:11.5px;line-height:1.5}

/* signup */
.signup{position:absolute;top:2612px;left:0;width:1200px;height:460px}
.perk{position:absolute;left:234px;width:400px}
.perk .tick{position:absolute;left:0;top:2px;width:14px;height:14px}
.perk h4{margin-left:22px;font-size:12.5px;line-height:17px;font-weight:500;color:var(--maroon)}
.perk p{margin-left:22px;margin-top:8px;font-size:12px;line-height:1.5;color:var(--muted)}
.signup-form{left:706px;top:138px;width:260px;height:273px;border:1px solid var(--line);background:#fafafa}
.signup-form h3{height:44px;line-height:44px;text-align:center;font-size:17px;background:#f1f1f1}
.field{position:absolute;left:20px;width:218px;height:30px;background:var(--white);border:1px solid var(--line);font-size:11px;color:#999;padding:8px 10px}
.field.is-top{border-color:#c8c8c8;color:var(--ink)}
.form-note{position:absolute;left:0;top:244px;width:100%;text-align:center;font-size:9px;color:var(--ink)}

/* newsletter */
.newsletter{position:absolute;top:3072px;left:0;width:1200px;height:153px;background:#f2f2f2}
.newsletter h3{left:234px;top:40px;font-size:22px;line-height:28px}
.newsletter p{left:234px;top:80px;width:420px;font-size:12px;line-height:1.5;color:var(--muted)}
.email-box{left:662px;top:42px;width:302px;height:52px;background:var(--white);border:1px solid var(--line);font-size:12px;color:#777;padding:16px 14px}
.send{right:0;top:0;width:52px;height:50px;background:var(--red)}

/* footer */
.site-footer{position:absolute;top:3225px;left:0;width:1200px;height:426px}
.site-footer .brand{left:0;width:1200px;justify-content:center;top:28px;font-size:24px}
.rule{left:234px;width:732px;height:1px;background:var(--line)}
.contact{left:234px;top:136px;font-size:11px;color:var(--muted);line-height:1.4}
.contact div{display:flex;gap:10px;margin-bottom:12px}
.contact svg{flex:none;margin-top:2px}
.link-col{position:absolute;top:136px;font-size:11px;color:var(--muted);line-height:18.5px;list-style:none}
.social{left:561px;top:360px;display:flex;gap:6px}
.social span{width:22px;height:22px;border-radius:50%;background:var(--red)}
.copyright{left:0;top:397px;width:1200px;text-align:center;font-size:10.5px;color:var(--muted)}
</style>
</head>
<body>

<header class="site-header">
  <div class="abs brand"><span class="brand-dot"></span>Merrow Prints</div>
  <div class="abs topbar"><span>Call for enquiry: <b>0198 552 3071</b></span><span>Sign in</span><span>Sign up</span></div>
  <nav class="abs main-nav">
    <span class="active">Products &amp; Pricing</span><span>How it works</span><span>Shipping</span><span>Resources</span><span>FAQ</span><span>Blog</span>
  </nav>
</header>

<section class="hero">
  <div class="abs ribbon">HURRY UP! 10% OFF</div>
  <h1 class="abs head center hero-title">We print all kind of gifts</h1>
  <p class="abs center hero-sub">Easy, on-demand, online printing, fulfillment and shipping.</p>
  <div class="btn btn-line" style="left:546px;top:142px;width:108px;height:34px">Get started</div>
  <div class="abs hero-gifts" role="img" aria-label="Illustration of wrapped gift boxes with red ribbons"></div>
</section>

<section class="split">
  <div class="split-half" style="left:0;background:var(--white)">
    <h3 class="head">Print designs for yourself</h3>
    <p>One-off designs that you want to have printed for your own use</p>
    <div class="btn btn-line" style="left:246px;top:119px;width:108px;height:34px">Get started</div>
  </div>
  <div class="split-half" style="left:600px;background:#eeeeee">
    <h3 class="head">Sell designs online</h3>
    <p>If you want to sell your designs in an online store or marketplace</p>
    <div class="btn btn-red" style="left:112px;top:119px;width:150px;height:34px">Connect your shop</div>
  </div>
  <div class="abs split-or">OR</div>
</section>

<section class="products">
  <h2 class="section-title head" style="top:42px">Our custom printed products</h2>
  <p class="section-sub" style="top:76px">Lorem ipsum dolor sit amet, consectetur adipiscing elit</p>

  <div class="product-card is-featured" style="left:234px;top:112px">
    <div class="product-art" role="img" aria-label="Backpack with colourful geometric print" style="background:linear-gradient(135deg,#3bb3a5,#e8503f 50%,#2c2c3a)"></div>
    <div class="product-label"><h4 class="head">Backpacks</h4><span>Starting from <b>$26.95</b></span>
      <svg class="abs go" viewBox="0 0 26 26"><path d="M11 8l5 5-5 5" fill="none" stroke="#fff" stroke-width="2"/></svg></div>
  </div>
  <div class="product-card" style="left:420px;top:112px">
    <div class="product-art" role="img" aria-label="Framed poster with bird illustration" style="background:linear-gradient(180deg,#f5efe6,#d8cfc2)"></div>
    <div class="product-label"><h4 class="head">Posters &amp; canvas prints</h4><span>Starting from <b>$7</b></span></div>
  </div>
  <div class="product-card" style="left:606px;top:112px">
    <div class="product-art" role="img" aria-label="Coffee mug with geometric print" style="background:linear-gradient(135deg,#f1b6a8,#5bbdb3 55%,#f4d38a)"></div>
    <div class="product-label"><h4 class="head">Coffee mugs</h4><span>Starting from <b>$8.95</b></span></div>
  </div>
  <div class="product-card" style="left:792px;top:112px">
    <div class="product-art" role="img" aria-label="Phone case with geometric print" style="background:linear-gradient(135deg,#f0a8b8,#6ec3c7 55%,#f5c06c)"></div>
    <div class="product-label"><h4 class="head">Phone case</h4><span>Starting from <b>$15.95</b></span></div>
  </div>

  <div class="product-card" style="left:234px;top:373px">
    <div class="product-art" role="img" aria-label="Throw pillow with small heart pattern" style="background:linear-gradient(180deg,#f7f7f7,#e3e3e3)"></div>
    <div class="product-label"><h4 class="head">Throw pillows</h4><span>Starting from <b>$13</b></span></div>
  </div>
  <div class="product-card" style="left:420px;top:373px">
    <div class="product-art" role="img" aria-label="Tote bag with dotted print" style="background:linear-gradient(180deg,#fafafa,#e6e6e6)"></div>
    <div class="product-label"><h4 class="head">Tote bags</h4><span>Starting from <b>$12</b></span></div>
  </div>
  <div class="product-card" style="left:606px;top:373px">
    <div class="product-art" role="img" aria-label="Framed poster with parrot illustration" style="background:linear-gradient(180deg,#f5efe6,#cfd8c6)"></div>
    <div class="product-label"><h4 class="head">Posters &amp; canvas prints</h4><span>Starting from <b>$7</b></span></div>
  </div>
  <div class="product-card" style="left:792px;top:373px">
    <div class="product-art" role="img" aria-label="Backpack with colourful geometric print" style="background:linear-gradient(135deg,#3bb3a5,#e8503f 50%,#2c2c3a)"></div>
    <div class="product-label"><h4 class="head">Backpacks</h4><span>Starting from <b>$26.95</b></span></div>
  </div>

  <div class="btn btn-red" style="left:526px;top:655px;width:148px;height:34px">Load more products</div>
</section>

<section class="how">
  <div class="abs how-wedge"></div>
  <h2 class="section-title head" style="top:40px">How it works</h2>
  <p class="section-sub" style="top:72px">Lorem ipsum dolor sit amet, consectetur adipiscing elit</p>

  <div class="step" style="left:209px">
    <div class="step-ring" style="left:60px"><div class="step-art" role="img" aria-label="Shop front icon"></div></div>
    <h4 class="head">Your store</h4>
    <p>Lorem ipsum dolor sit amet, consectetur adipiscing elit. Proin cursus eget sapien id eleifend. Morbi gravida malesuada venenatis fusce consectetur pulvinar.</p>
  </div>
  <svg class="abs step-arrow" style="left:423px" viewBox="0 0 84 10"><path d="M0 5h80M75 1l5 4-5 4" fill="none" stroke="#999" stroke-width="1.2"/></svg>
  <div class="step" style="left:479px">
    <div class="step-ring" style="left:60px"><div class="step-art" role="img" aria-label="Print factory icon"></div></div>
    <h4 class="head">Merrow factory</h4>
    <p>Lorem ipsum dolor sit amet, consectetur adipiscing elit. Proin cursus eget sapien id eleifend. Morbi gravida malesuada venenatis fusce consectetur pulvinar.</p>
  </div>
  <svg class="abs step-arrow" style="left:693px" viewBox="0 0 84 10"><path d="M0 5h80M75 1l5 4-5 4" fill="none" stroke="#999" stroke-width="1.2"/></svg>
  <div class="step" style="left:749px">
    <div class="step-ring" style="left:60px"><div class="step-art" role="img" aria-label="Delivery courier icon"></div></div>
    <h4 class="head">Your client</h4>
    <p>Lorem ipsum dolor sit amet, consectetur adipiscing elit. Proin cursus eget sapien id eleifend. Morbi gravida malesuada venenatis fusce consectetur pulvinar.</p>
  </div>
</section>

<section class="testimonials">
  <h2 class="section-title head" style="top:40px">What our customers speak</h2>
  <p class="section-sub" style="top:72px">Lorem ipsum dolor sit amet, consectetur adipiscing elit</p>
  <div class="abs quote-mark">&rdquo;</div>

  <div class="review" style="left:234px"><div class="stars">☆☆☆☆☆</div><p>Nunc accumsan leo quam, vel suscipit leo lobortis ut. Suspendisse eget hendrerit quam. Curabitur in odio nec libero ullamcorper iaculis. Praesent ornare augue at ante congue dapibus. Integer luctus mollis viverra.</p></div>
  <div class="review" style="left:485px"><div class="stars">☆☆☆☆☆</div><p>Nunc accumsan leo quam, vel suscipit leo lobortis ut. Suspendisse eget hendrerit quam. Curabitur in odio nec libero ullamcorper iaculis. Praesent ornare augue at ante congue dapibus. Integer luctus mollis viverra.</p></div>
  <div class="review" style="left:737px"><div class="stars">☆☆☆☆☆</div><p>Nunc accumsan leo quam, vel suscipit leo lobortis ut. Suspendisse eget hendrerit quam. Curabitur in odio nec libero ullamcorper iaculis. Praesent ornare augue at ante congue dapibus. Integer luctus mollis viverra.</p></div>
  <div class="reviewer" style="left:234px">James Porter</div>
  <div class="reviewer" style="left:485px">James Porter</div>
  <div class="reviewer" style="left:737px">James Porter</div>

  <div class="btn btn-red" style="left:526px;top:428px;width:148px;height:34px">Read all testimonials</div>
</section>

<section class="different">
  <div class="abs person-photo" role="img" aria-label="Photo of a smiling man carrying branded cardboard boxes"></div>
  <h2 class="section-title head" style="top:38px">What makes us different</h2>
  <p class="section-sub" style="top:72px">Lorem ipsum dolor sit amet, consectetur adipiscing elit</p>

  <div class="feature" style="left:492px;top:138px"><span class="num">01.</span><h4>Three fulfillment locations</h4><p>Nunc accumsan leo quam, vel suscipit leo lobortis ut. Suspendisse eget hendrerit quam. Curabitur in odio nec libero ullamcorper iaculis.</p></div>
  <div class="feature" style="left:735px;top:138px"><span class="num">02.</span><h4>Free signup, no monthly fees</h4><p>Nunc accumsan leo quam, vel suscipit leo lobortis ut. Suspendisse eget hendrerit quam. Curabitur in odio nec libero ullamcorper iaculis.</p></div>
  <div class="feature" style="left:492px;top:260px"><span class="num">03.</span><h4>Automated order import</h4><p>Nunc accumsan leo quam, vel suscipit leo lobortis ut. Suspendisse eget hendrerit quam. Curabitur in odio nec libero ullamcorper iaculis.</p></div>
  <div class="feature" style="left:735px;top:260px"><span class="num">04.</span><h4>Low shipping rates</h4><p>Nunc accumsan leo quam, vel suscipit leo lobortis ut. Suspendisse eget hendrerit quam. Curabitur in odio nec libero ullamcorper iaculis.</p></div>
</section>

<section class="signup">
  <h2 class="section-title head" style="top:40px">Create your Merrow Prints account for free</h2>
  <p class="section-sub" style="top:72px">Lorem ipsum dolor sit amet, consectetur adipiscing elit</p>

  <div class="perk" style="top:152px"><svg class="tick" viewBox="0 0 14 14"><circle cx="7" cy="7" r="6" fill="none" stroke="#e2342b" stroke-width="1.4"/><path d="M4 7l2 2 4-4" fill="none" stroke="#e2342b" stroke-width="1.4"/></svg><h4 class="head">No sign-up &amp; no monthly fees</h4><p>Nunc accumsan leo quam, vel suscipit leo lobortis ut. Suspendisse eget hendrerit quam. Curabitur in odio nec libero ullamcorper iaculis.</p></div>
  <div class="perk" style="top:232px"><svg class="tick" viewBox="0 0 14 14"><circle cx="7" cy="7" r="6" fill="none" stroke="#e2342b" stroke-width="1.4"/><path d="M4 7l2 2 4-4" fill="none" stroke="#e2342b" stroke-width="1.4"/></svg><h4 class="head">Discounts on sample orders</h4><p>Nunc accumsan leo quam, vel suscipit leo lobortis ut. Suspendisse eget hendrerit quam. Curabitur in odio nec libero ullamcorper iaculis.</p></div>
  <div class="perk" style="top:312px"><svg class="tick" viewBox="0 0 14 14"><circle cx="7" cy="7" r="6" fill="none" stroke="#e2342b" stroke-width="1.4"/><path d="M4 7l2 2 4-4" fill="none" stroke="#e2342b" stroke-width="1.4"/></svg><h4 class="head">More time for yourself</h4><p>Nunc accumsan leo quam, vel suscipit leo lobortis ut. Suspendisse eget hendrerit quam. Curabitur in odio nec libero ullamcorper iaculis.</p></div>

  <div class="abs signup-form">
    <h3 class="head">Free sign up</h3>
    <div class="field is-top" style="top:62px">Full Name</div>
    <div class="field" style="top:106px">Email</div>
    <div class="field" style="top:147px">Password</div>
    <div class="btn btn-red" style="left:87px;top:186px;width:86px;height:34px">Submit</div>
    <div class="form-note">By signing up you agree with Terms and Privacy Policy</div>
  </div>
</section>

<section class="newsletter">
  <h3 class="abs head">Newsletter subscription</h3>
  <p class="abs">Nunc accumsan leo quam, vel suscipit leo lobortis ut. Suspendisse eget hendrerit quam. Curabitur in odio nec libero ullamcorper iaculis.</p>
  <div class="abs email-box">Email Address
    <svg class="abs send" viewBox="0 0 52 50"><path d="M17 25l19-8-6 18-4-6z" fill="#fff"/></svg>
  </div>
</section>

<footer class="site-footer">
  <div class="abs brand"><span class="brand-dot"></span>Merrow Prints</div>
  <div class="abs rule" style="top:104px"></div>
  <div class="abs contact">
    <div><svg width="10" height="12" viewBox="0 0 10 12"><path d="M5 0a4 4 0 014 4c0 3-4 8-4 8S1 7 1 4a4 4 0 014-4z" fill="#e2342b"/><circle cx="5" cy="4" r="1.5" fill="#fff"/></svg><span>42, Elm Row, Dunmore,<br>New York 12480</span></div>
    <div><svg width="10" height="11" viewBox="0 0 10 11"><path d="M2 0l2 3-1 1.5c.6 1.3 1.4 2.2 2.5 2.7L7 6l3 2-1 2.5C5 10 1 6 0 1.5z" fill="#e2342b"/></svg><span>198 552 3071</span></div>
    <div><svg width="11" height="9" viewBox="0 0 11 9"><rect x=".5" y=".5" width="10" height="8" fill="none" stroke="#e2342b"/><path d="M.5.5l5 4 5-4" fill="none" stroke="#e2342b"/></svg><span>hello@merrowprints.com</span></div>
  </div>
  <ul class="link-col" style="left:448px"><li>Quality</li><li>Products &amp; Pricing</li><li>Volume discounts</li><li>Upcoming products</li><li>Shipping</li><li>Warehousing &amp; Fulfillment New</li><li>API</li><li>Mockup Generator</li><li>Policies</li></ul>
  <ul class="link-col" style="left:682px"><li>About us</li><li>Jobs New</li><li>Customers</li><li>Press</li><li>Blog</li><li>Reviews</li><li>Checklist</li><li>Profit Calculator</li><li>Feature Requests</li><li>Sitemap</li></ul>
  <ul class="link-col" style="left:842px"><li>FAQ</li><li>Merchandise</li><li>Affiliate</li><li>Merrow for celebrities</li><li>Important printing facts</li><li>Fabric printing guide</li><li>Screen printing</li></ul>
  <div class="abs rule" style="top:348px"></div>
  <div class="abs social"><span></span><span></span><span></span></div>
  <div class="abs copyright">2016 © Copyright, Merrow Prints, All Rights Reserved</div>
</footer>

</body>
</html>
```